Business cards design on a high standard

We advise clients on insurance and financial matters, since these clients pay for our advice, the design should have a high standard. Our logo should be included. From the colors we are open for everything.

Colors

Designer to choose colors to be used in the design.

```html
<!DOCTYPE html>
<html lang="en">
<head>
<meta charset="utf-8">
<title>Vantor Counsel – Business Cards</title>
<link href="https://fonts.googleapis.com/css2?family=Open+Sans:wght@400;600;700&display=swap" rel="stylesheet">
<style>
  :root {
    --bg: #3a3a3d;
    --card: #111112;
    --card-edge: #1c1c1e;
    --red: #e3191f;
    --grey: #a9a9ab;
    --faint: #262628;
  }
  * { margin: 0; padding: 0; box-sizing: border-box; }
  html, body { width: 1200px; height: 1200px; overflow: hidden; }
  body {
    background: radial-gradient(circle at 50% 40%, #5a5a5e 0%, var(--bg) 55%, #1e1e20 100%);
    font-family: "Open Sans", sans-serif;
    position: relative;
  }
  .card {
    position: absolute;
    left: 220px;
    width: 760px;
    height: 434px;
    border-radius: 26px;
    background: linear-gradient(160deg, var(--card-edge), var(--card) 60%);
    box-shadow: 0 18px 40px rgba(0,0,0,0.55);
    overflow: hidden;
  }
  .card--back { top: 120px; }
  .card--front { top: 640px; }

  .back-name {
    position: absolute;
    inset: 0;
    display: flex;
    align-items: center;
    justify-content: center;
    font-weight: 700;
    font-size: 62px;
    letter-spacing: 4px;
    color: var(--faint);
    text-transform: uppercase;
  }

  .brand {
    position: absolute;
    left: 56px;
    top: 58px;
    display: flex;
    align-items: center;
    gap: 14px;
  }
  .brand__dot {
    width: 22px; height: 22px;
    border-radius: 50%;
    background: var(--red);
  }
  .brand__name {
    font-weight: 700;
    font-size: 42px;
    letter-spacing: 2px;
    color: var(--red);
    text-transform: uppercase;
    line-height: 1;
  }

  .person {
    position: absolute;
    right: 62px;
    top: 176px;
    text-align: right;
  }
  .person__name {
    color: var(--red);
    font-size: 22px;
    letter-spacing: 7px;
    text-transform: uppercase;
    font-weight: 400;
  }
  .person__role {
    color: var(--grey);
    font-size: 17px;
    margin-top: 2px;
  }

  .rule {
    position: absolute;
    left: 60px;
    right: 60px;
    top: 252px;
    height: 2px;
    background: var(--red);
  }

  .address {
    position: absolute;
    left: 64px;
    top: 272px;
    color: var(--grey);
    font-size: 16px;
    line-height: 26px;
  }

  .contacts {
    position: absolute;
    right: 58px;
    top: 270px;
    list-style: none;
    color: var(--grey);
    font-size: 17px;
  }
  .contacts li {
    display: flex;
    align-items: center;
    justify-content: flex-end;
    gap: 10px;
    height: 30px;
  }
  .contacts svg { width: 16px; height: 16px; flex: none; }
</style>
</head>
<body>

  <section class="card card--back" aria-label="Card back">
    <div class="back-name">Vantor Counsel</div>
  </section>

  <section class="card card--front" aria-label="Card front">
    <div class="brand">
      <span class="brand__dot"></span>
      <span class="brand__name">Vantor Counsel</span>
    </div>

    <div class="person">
      <div class="person__name">Marcus Hale</div>
      <div class="person__role">President</div>
    </div>

    <div class="rule"></div>

    <address class="address" style="font-style:normal">
      P.O. Box 41800<br>
      Riverton, North Carolina 28150
    </address>

    <ul class="contacts">
      <li>700-555-0142
        <svg viewBox="0 0 16 16" aria-hidden="true"><path fill="var(--red)" d="M3.6 1.5l2.2 2.6-1.3 1.6c.9 2 2.4 3.6 4.4 4.6l1.6-1.3 2.6 2.2-1.2 2.3C6.7 14.9 1.4 9.6 1.5 3.3z"/></svg>
      </li>
      <li>mhale@vantorcounsel.com
        <svg viewBox="0 0 16 16" aria-hidden="true"><rect x="1" y="3.5" width="14" height="9.5" rx="1" fill="var(--red)"/><path d="M1.5 4.5L8 9l6.5-4.5" stroke="#111" stroke-width="1.2" fill="none"/></svg>
      </li>
      <li>www.vantorcounsel.com
        <svg viewBox="0 0 16 16" aria-hidden="true"><g fill="none" stroke="var(--red)" stroke-width="1.3"><circle cx="8" cy="8" r="6.5"/><ellipse cx="8" cy="8" rx="2.8" ry="6.5"/><path d="M1.5 8h13M2.5 4.8h11M2.5 11.2h11"/></g></svg>
      </li>
    </ul>
  </section>

</body>
</html>
```